Remo K Art Studio Business Card Layout

Hi, I have a logo but I need help laying it out on a business card. I would like to include the following:
The Logo (see attached)
remokartstudio.com
remo@remokartstudio.com

Industry/Entity Type

Business

```html
<!DOCTYPE html>
<html lang="en">
<head>
<meta charset="utf-8">
<title>Remo K Art Studio — Business Card</title>
<link href="https://fonts.googleapis.com/css2?family=Open+Sans:wght@400;600;700&display=swap" rel="stylesheet">
<style>
  :root {
    --backdrop: #0b1012;
    --card-white: #f4f4f4;
    --card-white-shade: #dcdcdc;
    --gold-light: #bcab7a;
    --gold-dark: #877955;
    --gold-mark: #c2a646;
    --bar-tint: #e2d8a6;
    --ink-light: #ffffff;
  }
  html, body {
    margin: 0;
    padding: 0;
    width: 1200px;
    height: 734px;
    overflow: hidden;
    background: var(--backdrop);
    font-family: "Open Sans", Arial, sans-serif;
  }
  .card {
    position: absolute;
    left: 100px;
    top: 82px;
    width: 1000px;
    height: 571px;
    overflow: hidden;
    box-shadow: 0 18px 40px rgba(0,0,0,0.6);
  }
  .card-art {
    position: absolute;
    inset: 0;
  }
  .studio-mark {
    position: absolute;
    left: 70px;
    top: 310px;
    display: flex;
    align-items: center;
    gap: 14px;
  }
  .studio-mark__dot {
    width: 22px;
    height: 22px;
    border-radius: 50%;
    background: var(--gold-mark);
  }
  .studio-mark__name {
    font-weight: 600;
    font-size: 30px;
    color: var(--gold-mark);
    letter-spacing: 0.5px;
    white-space: nowrap;
  }
  .holder {
    position: absolute;
    left: 672px;
    top: 98px;
    color: var(--ink-light);
    line-height: 1;
    white-space: nowrap;
  }
  .holder__name {
    font-weight: 700;
    font-size: 34px;
  }
  .holder__role {
    font-weight: 400;
    font-size: 21px;
    margin-top: 2px;
  }
  .contact {
    position: absolute;
    display: flex;
    align-items: center;
    gap: 12px;
    height: 46px;
    color: var(--ink-light);
    font-size: 21px;
    font-weight: 400;
    white-space: nowrap;
  }
  .contact svg { width: 20px; height: 20px; flex: none; }
  .contact--phone { left: 628px; top: 174px; }
  .contact--web { left: 644px; top: 229px; }
  .contact--mail { left: 660px; top: 284px; }
</style>
</head>
<body>
  <section class="card" aria-label="Remo K Art Studio business card">
    <svg class="card-art" viewBox="0 0 1000 571" width="1000" height="571" aria-hidden="true">
      <defs>
        <linearGradient id="paperFill" x1="0" y1="0" x2="1" y2="1">
          <stop offset="0" stop-color="var(--card-white-shade)"/>
          <stop offset="0.5" stop-color="var(--card-white)"/>
          <stop offset="1" stop-color="var(--card-white-shade)"/>
        </linearGradient>
        <linearGradient id="goldFill" x1="0" y1="0" x2="1" y2="1">
          <stop offset="0" stop-color="var(--gold-light)"/>
          <stop offset="1" stop-color="var(--gold-dark)"/>
        </linearGradient>
        <clipPath id="goldPanelClip">
          <polygon points="712,0 1000,0 1000,571 412,571"/>
        </clipPath>
      </defs>
      <rect class="paper" width="1000" height="571" fill="url(#paperFill)"/>
      <polygon class="accent-line" points="668,0 688,0 394,571 391,571" fill="url(#goldFill)"/>
      <polygon class="gold-panel" points="712,0 1000,0 1000,571 412,571" fill="url(#goldFill)"/>
      <g class="info-bars" clip-path="url(#goldPanelClip)" fill="var(--bar-tint)" opacity="0.28">
        <rect x="400" y="174" width="600" height="46"/>
        <rect x="400" y="229" width="600" height="46"/>
        <rect x="400" y="284" width="600" height="46"/>
        <rect x="400" y="360" width="600" height="46" opacity="0.6"/>
      </g>
    </svg>

    <div class="studio-mark">
      <span class="studio-mark__dot"></span>
      <span class="studio-mark__name">Remo K Art Studio</span>
    </div>

    <div class="holder">
      <div class="holder__name">John Doe</div>
      <div class="holder__role">Director</div>
    </div>

    <div class="contact contact--phone">
      <svg viewBox="0 0 24 24" aria-hidden="true"><path fill="#fff" d="M6.6 10.8a15 15 0 0 0 6.6 6.6l2.2-2.2c.3-.3.7-.4 1-.2 1.1.4 2.3.6 3.6.6.6 0 1 .4 1 1V20c0 .6-.4 1-1 1C10.6 21 3 13.4 3 4c0-.6.4-1 1-1h3.5c.6 0 1 .4 1 1 0 1.3.2 2.5.6 3.6.1.3 0 .7-.2 1z"/></svg>
      <span>61455019283</span>
    </div>
    <div class="contact contact--web">
      <svg viewBox="0 0 24 24" aria-hidden="true"><circle cx="12" cy="12" r="9" fill="none" stroke="#fff" stroke-width="2"/><ellipse cx="12" cy="12" rx="4" ry="9" fill="none" stroke="#fff" stroke-width="1.6"/><line x1="3" y1="12" x2="21" y2="12" stroke="#fff" stroke-width="1.6"/></svg>
      <span>remokartstudio.com</span>
    </div>
    <div class="contact contact--mail">
      <svg viewBox="0 0 24 24" aria-hidden="true"><text x="12" y="18" text-anchor="middle" font-family="Open Sans, Arial, sans-serif" font-size="20" font-weight="700" fill="#fff">@</text></svg>
      <span>remo@remokartstudio.com</span>
    </div>
  </section>
</body>
</html>
```